Party Decoration Set Designs - Rose Gold theme - more example images just added

We are looking for a set of designs for a set of party decorations. It’s a Rose Gold colored theme. I have attached some photos of some glittery rose gold items that I think would go good with the theme. There are also some photos of full sets of decorations in other colors schemes to give an idea of what we are looking for.

We would like to have designs for the items below:

1- Happy Birthday Flag Banner- looking for something unique. Size- 5”X7” WXL

2- hanging swirl cards ( photo examples attached) 4”X6” approx. can be different sizes and shapes.

3- centerpiece designs- photo examples attached. Middle
Piece that’s says Happy Birthday should be 5”X 7” and the smaller surrounding pieces 3X5

4 - round candy stickers and candy wrappers. Examples below. .75 inch

The photos below are of products currently sold. We would like to be very similar to these but just a little different to make our own. And then to have a Happy Birthday banner created to match the theme.

Some of these example photos below are from different themes and colors But I included them because they are the complete set we want to create. First we will do a generic “Happy Birthday” Set with rose gold glitter theme and then later we will add the Sweet 16 birthday theme as well and 40th, 50th etc.

On the centerpieces where the example photos how a large “40”, we would like this to be a larger “Happy Birthday” design. Then surrounded by some smaller designs.
I look forward to receiving your ideas

Target Market(s)

Anyone looking for birthday Peru decorations for a female.

Font styles to use
Other font styles liked:
• Open to designer suggestion

Requirements
Must have
• Happy Birthday Banner, Hanging swirl cards, centerpiece cards, cake topper
Nice to have
• We are certainly open to any creative ideas.
Should not have
• I just now added some example images of a very good set of exactly what we want but its in a different theme. This is a black gold set and our requested design is more feminine and Rose Gold color

```html
<!DOCTYPE html>
<html lang="en">
<head>
<meta charset="utf-8">
<title>Happy Birthday Flag Banner</title>
<link rel="stylesheet" href="https://fonts.googleapis.com/css2?family=Montserrat:wght@800&display=swap">
<style>
  :root {
    --canvas-bg: #ffffff;
    --gold-light: #f7d46a;
    --gold-mid: #e2a92c;
    --gold-deep: #c07f16;
    --flag-fill: #fcebe7;
    --letter: #b05a4f;
  }
  html, body {
    margin: 0;
    padding: 0;
    overflow: hidden;
    background: var(--canvas-bg);
  }
  .canvas {
    width: 1200px;
    height: 665px;
    overflow: hidden;
    background: var(--canvas-bg);
  }
  .banner { display: block; }
  .string {
    fill: none;
    stroke: url(#gold-sheen);
    stroke-width: 5;
    stroke-linecap: round;
  }
  .flag-border { fill: url(#gold-sheen); }
  .flag-face { fill: var(--flag-fill); }
  .flag-letter {
    font-family: "Montserrat", sans-serif;
    font-weight: 800;
    font-size: 74px;
    fill: var(--letter);
    text-anchor: middle;
    dominant-baseline: central;
  }
</style>
</head>
<body>
<main class="canvas">
  <svg class="banner" width="1200" height="665" viewBox="0 0 1200 665" role="img" aria-label="Happy Birthday flag banner">
    <defs>
      <linearGradient id="gold-sheen" x1="0" y1="0" x2="1" y2="1">
        <stop offset="0" stop-color="var(--gold-light)"/>
        <stop offset="0.5" stop-color="var(--gold-mid)"/>
        <stop offset="1" stop-color="var(--gold-deep)"/>
      </linearGradient>
      <g id="pennant">
        <path class="flag-border" d="M-68,0 H68 V168 L0,126 L-68,168 Z"/>
        <path class="flag-face" d="M-55,13 H55 V145 L0,111 L-55,145 Z"/>
      </g>
    </defs>

    <g transform="scale(0.8785)">
      <path class="string" d="M50,65 Q700,470 1300,45"/>
      <path class="string" d="M50,325 Q690,720 1320,360"/>

      <g class="banner-row banner-row--happy">
        <g class="flag" transform="translate(385,232) rotate(15)"><use href="#pennant"/><text class="flag-letter" x="0" y="72">H</text></g>
        <g class="flag" transform="translate(532,272) rotate(8)"><use href="#pennant"/><text class="flag-letter" x="0" y="72">A</text></g>
        <g class="flag" transform="translate(682,292) rotate(0)"><use href="#pennant"/><text class="flag-letter" x="0" y="72">P</text></g>
        <g class="flag" transform="translate(836,282) rotate(-8)"><use href="#pennant"/><text class="flag-letter" x="0" y="72">P</text></g>
        <g class="flag" transform="translate(990,226) rotate(-15)"><use href="#pennant"/><text class="flag-letter" x="0" y="72">Y</text></g>
      </g>

      <g class="banner-row banner-row--birthday">
        <g class="flag" transform="translate(145,368) rotate(20)"><use href="#pennant"/><text class="flag-letter" x="0" y="72">B</text></g>
        <g class="flag" transform="translate(292,438) rotate(15)"><use href="#pennant"/><text class="flag-letter" x="0" y="72">I</text></g>
        <g class="flag" transform="translate(442,486) rotate(10)"><use href="#pennant"/><text class="flag-letter" x="0" y="72">R</text></g>
        <g class="flag" transform="translate(604,514) rotate(3)"><use href="#pennant"/><text class="flag-letter" x="0" y="72">T</text></g>
        <g class="flag" transform="translate(764,516) rotate(-2)"><use href="#pennant"/><text class="flag-letter" x="0" y="72">H</text></g>
        <g class="flag" transform="translate(920,500) rotate(-8)"><use href="#pennant"/><text class="flag-letter" x="0" y="72">D</text></g>
        <g class="flag" transform="translate(1076,452) rotate(-12)"><use href="#pennant"/><text class="flag-letter" x="0" y="72">A</text></g>
        <g class="flag" transform="translate(1236,396) rotate(-18)"><use href="#pennant"/><text class="flag-letter" x="0" y="72">Y</text></g>
      </g>
    </g>
  </svg>
</main>
</body>
</html>
```